HUSH: Halt Usual Stuff Happily school library event

I need two poster designs for Halt Usual Stuff Happily (HUSH) in BC, requested by the CSMKA--Cedarvale School Media Keepers' Association. One should be for elementary students and one for high school. I want the date (Monday, October 26, 2020) and Halt Usual Stuff Happily. I would like the posters in English and in French. French is : Mets Ta Journée En Pause! I'm including last year's posters as examples. I would like to be able to print the poster files on 11x17 paper.

Requirements
Must have
• -The phrase "Halt Usual Stuff Happily" for the English version; "Mets Ta Journée En Pause" for the French version.
-Include the organization name: Cedarvale School Media Keepers' Association
-The date: Monday, October 26, 2020
Nice to have
• I would like the elementary version to be bright and colourful--fun for younger kids. I would like the high school version to be a bit more mature for the older students. Can still be bright and colourful.

```html
<!DOCTYPE html>
<html lang="fr">
<head>
<meta charset="utf-8">
<title>CHUT — Mets Ta Journée En Pause</title>
<link rel="stylesheet" href="https://fonts.googleapis.com/css2?family=Poppins:wght@300;400;500;600;700&family=Gochi+Hand&display=swap">
<style>
  :root {
    --page: #ffffff;
    --sky: #1e9bd6;
    --book: #16649a;
    --spine: #0f578a;
    --sun: #f6dc0c;
    --ink: #2e1a45;
    --paper: #ffffff;
  }
  * { margin: 0; padding: 0; box-sizing: border-box; }
  html, body {
    width: 1200px;
    height: 1200px;
    overflow: hidden;
    background: var(--page);
  }
  .poster {
    position: absolute;
    left: 262px;
    top: 78px;
    width: 675px;
    height: 1043px;
    background: var(--sky);
    overflow: hidden;
  }
  .bubble {
    position: absolute;
    left: 0;
    top: 0;
    width: 675px;
    height: 580px;
  }
  .bubble-shape { fill: var(--sun); }
  .bubble-word {
    position: absolute;
    left: 0;
    width: 675px;
    top: 228px;
    text-align: center;
    font-family: "Poppins", sans-serif;
    font-weight: 700;
    font-size: 138px;
    line-height: 1;
    letter-spacing: 6px;
    color: var(--ink);
  }
  .tagline {
    position: absolute;
    left: 0;
    width: 675px;
    top: 588px;
    text-align: center;
    font-family: "Gochi Hand", cursive;
    font-size: 38px;
    letter-spacing: 1px;
    color: var(--paper);
  }
  .book-art {
    position: absolute;
    left: 65px;
    top: 741px;
    width: 545px;
    height: 302px;
    background: var(--book);
  }
  .book-spine {
    position: absolute;
    left: 255px;
    top: 0;
    width: 42px;
    height: 100%;
    background: var(--spine);
  }
  .organisation {
    position: absolute;
    left: 93px;
    top: 920px;
    font-family: "Poppins", sans-serif;
    font-weight: 300;
    font-size: 17.5px;
    line-height: 31px;
    letter-spacing: 0.6px;
    color: var(--paper);
  }
  .event-date {
    position: absolute;
    left: 385px;
    top: 882px;
    width: 210px;
    font-family: "Poppins", sans-serif;
    color: var(--paper);
    transform: rotate(3deg);
    transform-origin: left top;
  }
  .event-date span { display: block; line-height: 1.05; }
  .event-day { font-weight: 600; font-size: 33px; padding-left: 28px; }
  .event-daymonth { font-weight: 500; font-size: 35px; }
  .event-year { font-weight: 500; font-size: 35px; padding-left: 28px; }
</style>
</head>
<body>
  <main class="poster">
    <svg class="bubble" viewBox="0 0 675 580" aria-hidden="true">
      <circle class="bubble-shape" cx="338" cy="301" r="219"/>
      <polygon class="bubble-shape" points="308,505 366,505 338,567"/>
    </svg>
    <h1 class="bubble-word">CHUT</h1>
    <p class="tagline">Mets Ta Journée En Pause</p>

    <div class="book-art" role="img" aria-label="Illustration d’un livre ouvert tenu par un lecteur qui regarde par-dessus">
      <div class="book-spine"></div>
    </div>

    <p class="organisation">Cedarvale School<br>Media Keepers’<br>Association</p>

    <p class="event-date">
      <span class="event-day">Lundi</span>
      <span class="event-daymonth">26 Octobre</span>
      <span class="event-year">2020</span>
    </p>
  </main>
</body>
</html>
```